LumaVantix
stationery - business cards
LumaVantix -
Creative Brief
Professional
Carl MORVEDO
41 Pellin Lane, suite 218 Brenwick, Oregon, 97950
cm@lumavantix.com
www.lumavantix.com
Free to be creative

```html
<!DOCTYPE html>
<html lang="en">
<head>
<meta charset="utf-8">
<title>LumaVantix Stationery</title>
<link href="https://fonts.googleapis.com/css2?family=Source+Sans+3:wght@400;600&display=swap" rel="stylesheet">
<style>
:root{
  --blue:#1a6fc4;
  --blue-light:#5aa0e6;
  --blue-dark:#0f56a3;
  --gray:#8c8f93;
  --text:#555a60;
  --paper:#ffffff;
  --bg:#ffffff;
}
*{margin:0;padding:0;box-sizing:border-box}
html,body{width:1200px;height:1025px;overflow:hidden;background:var(--bg);font-family:"Source Sans 3",Arial,sans-serif;color:var(--text)}
.canvas{position:relative;width:1200px;height:1025px}
.sheet{position:absolute;background:var(--paper);box-shadow:0 0 0 1px #d6d8db,2px 3px 6px rgba(0,0,0,.12)}
.brand{position:absolute;display:flex;align-items:center;gap:12px;white-space:nowrap}
.brand-square{flex:none;background:var(--blue);border-radius:5px}
.brand-name{font-weight:600;color:var(--blue);letter-spacing:.5px;line-height:1}
.letterhead{left:33px;top:22px;width:743px;height:974px}
.letterhead .brand{left:24px;top:82px}
.letterhead .brand-square{width:54px;height:54px}
.letterhead .brand-name{font-size:52px}
.letterhead-footer{position:absolute;left:30px;top:880px;font-size:15px;line-height:28px;color:var(--text)}
.stripe{position:absolute;left:0;width:100%}
.letterhead .stripe{bottom:16px;height:24px}
.envelope{left:39px;top:474px;width:818px;height:357px}
.envelope .brand{left:24px;top:48px}
.envelope .brand-square{width:54px;height:54px}
.envelope .brand-name{font-size:52px}
.envelope-address{position:absolute;left:24px;top:308px;font-size:15px}
.envelope .stripe{bottom:0;height:26px}
.flap{position:absolute;left:39px;top:352px;width:826px;height:124px}
.card{position:absolute;left:887px;width:299px}
.card-front{top:390px;height:230px}
.card-front .brand{left:16px;top:18px;gap:7px}
.card-front .brand-square{width:24px;height:24px;border-radius:3px}
.card-front .brand-name{font-size:23px}
.card-person{position:absolute;left:100px;top:70px;font-size:14px;color:var(--blue)}
.card-details{position:absolute;left:16px;top:98px;font-size:10.5px;line-height:14px}
.card-front .stripe{bottom:0;height:10px}
.card-back{top:642px;height:175px;background:radial-gradient(ellipse at 50% 40%,var(--blue-light),var(--blue) 55%,var(--blue-dark));box-shadow:1px 2px 5px rgba(0,0,0,.15)}
.card-back .brand{left:0;right:0;top:40px;justify-content:center;gap:9px}
.card-back .brand-square{width:30px;height:30px;background:#fff;border-radius:4px}
.card-back .brand-name{font-size:30px;color:#fff}
.card-tagline{position:absolute;left:0;right:0;top:128px;text-align:center;font-size:14px;color:#fff}
</style>
</head>
<body>
<main class="canvas">

  <section class="sheet letterhead" aria-label="Letterhead">
    <div class="brand"><span class="brand-square"></span><span class="brand-name">LumaVantix</span></div>
    <div class="letterhead-footer">
      <p>41 Pellin Lane, suite 218 Brenwick, Oregon, 97950</p>
      <p>Phone: (541) 555-0142 | www.lumavantix.com</p>
    </div>
    <svg class="stripe" viewBox="0 0 743 24" preserveAspectRatio="none">
      <defs><linearGradient id="lhBlue" x1="0" x2="1"><stop offset="0" stop-color="#1a6fc4"/><stop offset=".5" stop-color="#5aa0e6"/><stop offset="1" stop-color="#1a6fc4"/></linearGradient></defs>
      <rect width="743" height="24" fill="url(#lhBlue)"/>
      <polygon points="600,0 743,0 743,24 575,24" fill="#8c8f93"/>
    </svg>
  </section>

  <svg class="flap" viewBox="0 0 826 124" preserveAspectRatio="none" aria-label="Envelope flap">
    <defs><linearGradient id="flapBlue" x1="0" x2="1"><stop offset="0" stop-color="#0f56a3"/><stop offset=".5" stop-color="#5aa0e6"/><stop offset="1" stop-color="#0f56a3"/></linearGradient></defs>
    <polygon points="0,124 40,0 790,0 826,124" fill="url(#flapBlue)"/>
    <rect x="381" y="30" width="64" height="64" rx="8" fill="#ffffff"/>
  </svg>

  <section class="sheet envelope" aria-label="Envelope">
    <div class="brand"><span class="brand-square"></span><span class="brand-name">LumaVantix</span></div>
    <p class="envelope-address">41 Pellin Lane, suite 218 Brenwick, Oregon, 97950</p>
    <svg class="stripe" viewBox="0 0 818 26" preserveAspectRatio="none">
      <defs><linearGradient id="envBlue" x1="0" x2="1"><stop offset="0" stop-color="#1a6fc4"/><stop offset=".5" stop-color="#5aa0e6"/><stop offset="1" stop-color="#1a6fc4"/></linearGradient></defs>
      <rect width="818" height="26" fill="url(#envBlue)"/>
      <polygon points="680,0 818,0 818,26 655,26" fill="#8c8f93"/>
    </svg>
  </section>

  <section class="sheet card card-front" aria-label="Business card front">
    <div class="brand"><span class="brand-square"></span><span class="brand-name">LumaVantix</span></div>
    <p class="card-person">Carl MORVEDO</p>
    <div class="card-details">
      <p>41 Pellin Lane, suite 218</p>
      <p>Brenwick, Oregon, 97950</p>
      <p>Phone: (541) 555-0142</p>
      <p>Email: cm@lumavantix.com</p>
      <p>www.lumavantix.com</p>
    </div>
    <svg class="stripe" viewBox="0 0 299 10" preserveAspectRatio="none">
      <rect width="299" height="10" fill="#1a6fc4"/>
    </svg>
  </section>

  <section class="card card-back" aria-label="Business card back">
    <div class="brand"><span class="brand-square"></span><span class="brand-name">LumaVantix</span></div>
    <p class="card-tagline">Free to be creative</p>
  </section>

</main>
</body>
</html>
```